Flyer-Design für Gefäßchirurg
Zielgruppe
Niedergelassener Gefäßchirurg in eigener (Einzel-) Praxis; zZt 4 Angestellte (1 Krankenschwester, eine MFA, eine Azubi, eine Reinigungskraft); tätig in der Stadt Plön (24306); im Kreis Plön nur ein weiter ALLGEMEIN chirurg; HP: www.praxisdoktor-haverbeck.de ; Kernkompetenz: Diagnostik und Therapie von Gefäßerkrankungen (z.B. Krampfadern, Durchblutungsstörungen... (s.auch HP); eigener OP in der Praxis; hier Versorgung u.a. von Krampfadern aber auch andere chirurgische Eingriffe;
Aufgabenstellung
Bzgl. des Formates keine Festlegung bevorzuge aber Format Din lang hoch oder Din a 5 hoch ; Flyer soll übersichtlich Behandlungen der Praxis benennen; insbesondere um auch außerhalb der Gefäßchirurgie weitere chirurgische Patienten zu gewinnen (z.B. chirurgische Entfernung kleiner Pigmentflecke, eingewachsener Nagel, aber auch 'Wegspritzen/ Sklerosierung' von Besenreisern, eingewachsener Zehennagel), ggf. mit Anfahrtskarte, Parkplätze vor der Tür; falls nicht zu Kostenintensiv: auch Nutzung von Stock - Bildern (ca. Obergrenze für Bildmaterial 50,- €);
mir ist bewusst, dass die Photos der Angestellten und mir nicht 100% scharf sind; falls diese verwendet werden, könnten diese z.B. kleinformatig auf dem flyer erscheinen, oder ich würde diese im Verlauf noch einmal aufnehmen. Ob und wieviele der Photos auf dem flyer sind, überlasse ich Ihnen.

```html
<!DOCTYPE html>
<html lang="de">
<head>
<meta charset="utf-8">
<title>Flyer – Praxis für Gefäßmedizin und Chirurgie</title>
<link href="https://fonts.googleapis.com/css2?family=Ubuntu:wght@400;500&family=Arimo:wght@400;700&display=swap" rel="stylesheet">
<style>
  :root{
    --red:#c4161c;
    --red-deep:#8e0c10;
    --red-bright:#e0262a;
    --salmon:#e9a797;
    --salmon-deep:#c8705c;
    --ink:#3a3a3a;
    --ink-soft:#555;
    --stage:#dcdcdc;
  }
  *{box-sizing:border-box;margin:0;padding:0}
  html,body{width:1200px;height:765px;overflow:hidden}
  body{background:var(--stage);font-family:"Arimo",Arial,sans-serif;color:var(--ink);position:relative}

  .spread{position:absolute;top:132px;width:500px;height:500px;display:flex;box-shadow:0 10px 24px rgba(0,0,0,.25);overflow:hidden}
  .spread--inside{left:70px}
  .spread--outside{left:630px}
  .panel{position:relative;width:250px;height:500px;overflow:hidden}

  .panel-welcome{background:linear-gradient(180deg,#ececec 0%,#fbfbfb 30%,#e4e4e4 100%)}
  .panel-services{background:linear-gradient(160deg,#c6c6c6 0%,#dedede 45%,#ececec 100%)}
  .facets{position:absolute;inset:0 0 auto 0;width:100%;height:60px}

  .section-title{font-family:"Ubuntu",sans-serif;font-weight:400;color:var(--red);font-size:9px}
  .section-title--ruled{display:inline-block;padding-bottom:3px;border-bottom:1px dotted var(--red)}

  .welcome{position:absolute;left:22px;top:58px;width:210px;font-size:7.6px;line-height:10px;color:var(--ink-soft)}
  .welcome .section-title{margin-bottom:6px}
  .welcome p{margin-bottom:10px}
  .welcome b{color:var(--ink)}

  .brand{position:absolute;left:26px;top:66px}
  .brand-name{font-family:"Ubuntu",sans-serif;font-weight:500;font-size:17px;color:#444;display:flex;align-items:center;gap:6px}
  .brand-mark{width:7px;height:7px;background:var(--red);display:inline-block}
  .brand-sub{font-family:"Ubuntu",sans-serif;font-size:9.5px;color:#555;margin-top:2px;padding-left:13px}

  .services{position:absolute;left:26px;top:135px;width:212px}
  .services ul{list-style:none;margin-top:8px;font-family:"Ubuntu",sans-serif;font-size:8px;line-height:11px;color:#444}
  .services li{position:relative;padding-left:13px;margin-bottom:2px}
  .services li::before{content:"";position:absolute;left:2px;top:4px;width:2.5px;height:2.5px;background:#444;border-radius:50%}

  .cell-band{position:absolute;left:0;top:318px;width:500px;height:182px;
    background:radial-gradient(circle at 70% 30%,#f2c2b6 0%,transparent 45%),linear-gradient(120deg,var(--salmon) 0%,#d98b78 55%,var(--salmon-deep) 100%)}
  .profile-card{position:absolute;left:60px;top:352px;width:400px;height:76px;background:#f4f4f4;box-shadow:0 2px 6px rgba(0,0,0,.2)}
  .portrait{position:absolute;left:22px;top:338px;width:92px;height:112px;background:linear-gradient(160deg,#9a9a9a,#5d5d5d);border:3px solid #fff;box-shadow:0 2px 6px rgba(0,0,0,.3)}
  .bio{position:absolute;left:124px;top:358px;width:330px}
  .bio h3{font-family:"Ubuntu",sans-serif;font-weight:400;color:var(--red);font-size:10px}
  .bio ul{list-style:none;font-size:6.1px;line-height:8px;color:#444;margin-top:2px}
  .bio li{position:relative;padding-left:8px}
  .bio li::before{content:"";position:absolute;left:1px;top:3px;width:2px;height:2px;background:#444;border-radius:50%}

  .panel-contact{background:linear-gradient(160deg,#ededed 0%,#dcdcdc 40%,#c9c9c9 100%);padding:24px 22px 0 28px;font-size:6.8px;line-height:8.8px;color:var(--ink-soft)}
  .panel-contact .section-title{margin-bottom:7px}
  .panel-contact p{margin-bottom:7px}
  .panel-contact b{color:var(--ink)}
  .hours{margin:4px 0 18px;border-collapse:collapse;font-size:6.6px;color:var(--ink-soft)}
  .hours caption{text-align:left;font-weight:700;font-size:7.4px;color:var(--ink);padding-bottom:2px}
  .hours td{padding:0 14px 0 0;line-height:8.6px}
  .contact-block{margin-bottom:8px}
  .map{position:absolute;left:24px;top:400px;width:140px;height:100px;background:linear-gradient(135deg,#eaeaea 0%,#e2e2e2 60%,#b9d4e0 100%);border:1px solid #999}
  .vertical-url{position:absolute;left:184px;top:490px;transform:rotate(-90deg);transform-origin:left top;font-family:"Ubuntu",sans-serif;font-size:8px;color:var(--red);white-space:nowrap;letter-spacing:.2px}

  .panel-cover{background:radial-gradient(circle at 55% 55%,#e03a33 0%,transparent 40%),radial-gradient(circle at 30% 80%,#b01518 0%,transparent 45%),linear-gradient(160deg,var(--red-bright) 0%,var(--red) 45%,var(--red-deep) 100%)}
  .cover-card{position:absolute;left:22px;top:28px;width:206px;height:150px;background:#f5f5f5;box-shadow:0 2px 8px rgba(0,0,0,.3);padding:62px 0 0 16px}
  .cover-card .brand-name{font-size:15px}
  .cover-card .brand-sub{font-size:9px}
  .address-card{position:absolute;left:34px;top:390px;width:180px;height:96px;background:#f5f5f5;box-shadow:0 2px 8px rgba(0,0,0,.3);text-align:center;padding-top:18px;font-family:"Ubuntu",sans-serif;color:#444}
  .address-card .street{font-size:10px}
  .address-card .city{font-size:10px;font-weight:500}
  .address-card .url{display:block;margin:12px auto 0;width:150px;border-top:1px dotted var(--red);padding-top:9px;font-family:"Arimo",sans-serif;font-size:6.4px;color:var(--red)}
</style>
</head>
<body>

<section class="spread spread--inside" aria-label="Flyer Innenseite">
  <div class="panel panel-welcome">
    <svg class="facets" viewBox="0 0 250 60" preserveAspectRatio="none" aria-hidden="true">
      <polygon points="0,0 250,0 120,40" fill="#e0d2cf"/>
      <polygon points="120,40 250,0 250,50" fill="#ebe4e2"/>
    </svg>
    <div class="welcome">
      <h2 class="section-title">Ich begrüße Sie herzlich in unserer Praxis!</h2>
      <p>Gerne kümmern wir uns um Ihre <b>gefäßmedizinischen und chirurgischen Anliegen.</b></p>
      <p>Als <b>Gefäßchirurg und Phlebologe</b> besitze ich eine besondere Erfahrung in der Therapie und Diagnostik von gefäßmedizinischen Erkrankungen.</p>
      <p>Mit einem hochwertigen <b>Ultraschallgerät</b> sowie durch einen in die Praxis integrierten <b>Operationsraum</b> und einem <b>Aufwachraum</b> sind optimale Bedingungen gegeben.</p>
      <p>Bezüglich der operativen Versorgung des <b>Krampfaderleidens</b> halten wir alle gängigen Operationsmethoden vor.</p>
      <p>Abseits der gefäßmedizinischen Erkrankungen sind wir auch für <b>kleinere chirurgischen Maßnahmen</b> Ihr Ansprechpartner.</p>
    </div>
  </div>

  <div class="panel panel-services">
    <svg class="facets" viewBox="0 0 250 60" preserveAspectRatio="none" aria-hidden="true">
      <polygon points="0,0 250,0 250,45 150,20" fill="#e6dcda"/>
    </svg>
    <div class="brand">
      <div class="brand-name"><span class="brand-mark"></span>Dr. Jonas Haverbeck</div>
      <div class="brand-sub">Gefäßmedizin und Chirurgie</div>
    </div>
    <div class="services">
      <h2 class="section-title section-title--ruled">Leistungen</h2>
      <ul>
        <li>Krampfadern</li>
        <li>Besenreiser</li>
        <li>Schaufensterkrankheit - Durchblutungsstörung der Beine</li>
        <li>Bauchaortenaneurysma - Erweiterungen der Bauch- und Beckenschlagader</li>
        <li>Bewertung des Schlaganfallsrisikos</li>
        <li>Durchblutungsstörung der Hände und Füße</li>
        <li>Pigmentflecken oder kleine Hauttumore</li>
        <li>Nagelbettentzündung</li>
        <li>Steißbeinfistel</li>
      </ul>
    </div>
  </div>

  <div class="cell-band" role="img" aria-label="Nahaufnahme roter Blutkörperchen in zartem Rosé"></div>
  <div class="profile-card"></div>
  <div class="portrait" role="img" aria-label="Porträtfoto des Arztes in Schwarzweiß"></div>
  <div class="bio">
    <h3>Dr. Jonas Haverbeck</h3>
    <ul>
      <li>Ehemals leitender Oberarzt Klinik für Gefäßmedizin in Nordstadt</li>
      <li>Endovaskulärer Chirurg</li>
      <li>Weiterbildung zum Phlebologen („Venenspezialist“)</li>
      <li>Prüfung in der Ultraschalldiagnostik</li>
      <li>Doppler/ Duplexsonographie extrakranieller Gefäße (Gefäße des Halses)</li>
      <li>Ultraschalldiagnostik Doppler/ Duplexsonographie der peripheren Venen und Arterien</li>
    </ul>
  </div>
</section>

<section class="spread spread--outside" aria-label="Flyer Außenseite">
  <div class="panel panel-contact">
    <h2 class="section-title section-title--ruled">Terminvergabe</h2>
    <p>Wir bieten unseren Patienten eine <b>Terminsprechstunde</b> an. Dies hat den Vorteil, dass Wartezeiten auf ein Minimum beschränkt werden.</p>
    <p>Gerne vergeben wir Ihnen unter Telefon <b>04711 5518300</b> einen für Sie passenden Termin.</p>
    <p>Für ein akutes Problem wenden Sie sich bitte an die entsprechenden Einrichtungen, alternativ bieten wir auch zu bestimmten Zeiten eine offene Sprechstunde an. Diese Zeiten entnehmen Sie der Internetpräsenz der regionalen Ärztevereinigung Nordland.</p>
    <table class="hours">
      <caption>Öffnungszeiten</caption>
      <tr><td>Montag:</td><td>8:00 - 13:00</td><td></td></tr>
      <tr><td>Dienstag:</td><td>8:00 - 13:00</td><td>15:00 - 18:00</td></tr>
      <tr><td>Mittwoch:</td><td>8:00 - 13:00</td><td></td></tr>
      <tr><td>Donnerstag:</td><td>8:00 - 13:00</td><td></td></tr>
      <tr><td>Freitag:</td><td>8:00 - 13:00</td><td></td></tr>
    </table>
    <h2 class="section-title section-title--ruled">Anfahrt &amp; Kontakt</h2>
    <p class="contact-block">Dr. Jonas Haverbeck<br>Praxis für Gefäßmedizin, Gefäßchirurgie<br>und Phlebologie</p>
    <p class="contact-block">Lindenweg 12<br>23999 Haverstedt</p>
    <p class="contact-block">04711 5518 300<br>04711 5518 309<br>info@praxisdoktor-haverbeck.de</p>
    <div class="map" role="img" aria-label="Lageplan der Praxis mit Straßen, Seen und Parkplätzen"></div>
    <span class="vertical-url">www.praxisdoktor-haverbeck.de</span>
  </div>

  <div class="panel panel-cover" role="img" aria-label="Rote Blutkörperchen im Blutstrom">
    <div class="cover-card">
      <div class="brand-name"><span class="brand-mark"></span>Dr. Jonas Haverbeck</div>
      <div class="brand-sub">Gefäßmedizin und Chirurgie</div>
    </div>
    <div class="address-card">
      <div class="street">Lindenweg 12</div>
      <div class="city">23999 Haverstedt</div>
      <span class="url">www.praxisdoktor-haverbeck.de</span>
    </div>
  </div>
</section>

</body>
</html>
```